Dental Plan for Dogs

We are a vet clinic and I am wanting a poster designed that can then ultimately be changed/rejigged to be use on a website/facebook as a banner ad that promotes dental health in dogs. Therefore I will need the photoshop files as well as pngs/pdfs.
I want a dog and a cat in the image used for the poster with them showing healthy teeth and looking happy!
The feels is to be professional but also cute/funny. Using the orange coming through from the logo and the logo somewhere on the poster.
The text as below
Heading: Join our Dental Evergreen Plan!
Text: Keep your fur child smiling all year round while we cap their dental work at $365 if they return for a dental clean within 365 days! The plan includes full mouth dental x-rays and scale and polish of all teeth under a carefully monitored general anaesthetic! That'll give you both a reason to smile and save you over $180 per dental! *
Conditions (in smaller writing): *Any extractions and more advanced dental procedures if required will incur an additional cost that will be discussed with your prior to the procedure.
Thanks

```html
<!DOCTYPE html>
<html lang="en">
<head>
<meta charset="utf-8">
<title>Join our Dental Evergreen Plan – Maple Lane Vet Clinic</title>
<link rel="stylesheet" href="https://fonts.googleapis.com/css2?family=Fredoka:wght@300;400;600;700&display=swap">
<style>
  :root {
    --brown: #6b5447;
    --brown-dark: #5c473b;
    --orange: #f7941d;
    --orange-light: #fbb04a;
    --white: #ffffff;
    --cream: #fff7ec;
  }
  html, body {
    margin: 0;
    padding: 0;
    width: 848px;
    height: 1200px;
    overflow: hidden;
    background: var(--brown);
  }
  .poster {
    position: relative;
    width: 848px;
    height: 1200px;
    overflow: hidden;
    background: var(--brown);
    font-family: "Fredoka", sans-serif;
    color: var(--white);
  }
  .poster__backdrop {
    position: absolute;
    inset: 0;
  }
  .clinic {
    position: absolute;
    left: 24px;
    top: 40px;
    width: 250px;
    text-align: center;
  }
  .clinic__name {
    margin: 0;
    font-weight: 600;
    font-size: 36px;
    line-height: 1.05;
    color: var(--orange);
  }
  .clinic__area {
    margin: 14px 0 0;
    font-weight: 600;
    font-size: 22px;
    letter-spacing: 0.04em;
    color: var(--orange);
  }
  .headline {
    position: absolute;
    right: 30px;
    top: 22px;
    margin: 0;
    text-align: right;
    font-weight: 700;
    line-height: 1;
  }
  .headline__line { display: block; }
  .headline__line--intro { font-size: 60px; color: var(--white); }
  .headline__line--accent { font-size: 82px; color: var(--orange); margin-top: 8px; }
  .headline__line--accent-long { font-size: 70px; color: var(--orange); margin-top: 10px; }
  .headline__line--close { font-size: 64px; color: var(--white); margin-top: 12px; }
  .pet-illustration {
    position: absolute;
    left: 26px;
    top: 700px;
    width: 152px;
    height: 118px;
    border-radius: 50% 50% 40% 40%;
    background: radial-gradient(circle at 40% 45%, #8a5a3a 0 40%, #b9b4b0 41% 75%, transparent 76%);
  }
  .offer {
    position: absolute;
    left: 46px;
    top: 818px;
    width: 780px;
    margin: 0;
    font-weight: 700;
    font-size: 28px;
    line-height: 1.15;
  }
  .details {
    position: absolute;
    left: 46px;
    top: 928px;
    width: 790px;
    margin: 0;
    font-weight: 300;
    font-size: 30px;
    line-height: 1.15;
  }
  .footnote {
    position: absolute;
    left: 0;
    right: 0;
    top: 1162px;
    margin: 0;
    text-align: center;
    font-weight: 400;
    font-size: 10.5px;
    color: var(--cream);
  }
</style>
</head>
<body>
<main class="poster">
  <svg class="poster__backdrop" width="848" height="1200" viewBox="0 0 848 1200" aria-hidden="true">
    <defs>
      <radialGradient id="catTones" cx="45%" cy="45%" r="60%">
        <stop offset="0" stop-color="#b08f78"/>
        <stop offset="0.6" stop-color="#6e5b4f"/>
        <stop offset="1" stop-color="#3f3630"/>
      </radialGradient>
      <radialGradient id="dogTones" cx="50%" cy="50%" r="60%">
        <stop offset="0" stop-color="#8e8e92"/>
        <stop offset="0.6" stop-color="#3d3f45"/>
        <stop offset="1" stop-color="#23252a"/>
      </radialGradient>
    </defs>
    <rect width="848" height="1200" fill="var(--brown)"/>
    <path d="M0 505 C150 520 260 770 430 765 C600 760 720 610 848 545 L848 1140 L0 1140 Z" fill="var(--orange-light)"/>
    <path d="M0 522 C150 540 260 790 430 785 C600 780 720 630 848 565 L848 1140 L0 1140 Z" fill="var(--orange)"/>
    <rect x="0" y="1140" width="848" height="60" fill="var(--brown-dark)"/>
    <circle cx="325" cy="413" r="222" fill="var(--white)"/>
    <circle cx="325" cy="413" r="211" fill="url(#catTones)" role="img" aria-label="Photo: close-up of a yawning tabby cat showing clean teeth"/>
    <circle cx="598" cy="525" r="132" fill="var(--white)"/>
    <circle cx="598" cy="525" r="122" fill="url(#dogTones)" role="img" aria-label="Photo: happy black and white border collie smiling"/>
  </svg>

  <header class="clinic">
    <p class="clinic__name">Maple Lane<br>Vet Clinic</p>
    <p class="clinic__area">HILLCREST</p>
  </header>

  <h1 class="headline">
    <span class="headline__line headline__line--intro">Join our</span>
    <span class="headline__line headline__line--accent">Dental</span>
    <span class="headline__line headline__line--accent-long">Evergreen</span>
    <span class="headline__line headline__line--close">Plan!</span>
  </h1>

  <div class="pet-illustration" role="img" aria-label="Illustration: cartoon puppy and kitten cuddling"></div>

  <p class="offer">Keep your fur child smiling all year round while we cap their dental work at $365 if they return for a dental clean within 365 days!</p>

  <p class="details">The plan includes full mouth dental x-rays and scale and polish of all teeth under a carefully monitored general anaesthetic! That'll give you both a reason to smile and save you over $180 per dental! *</p>

  <p class="footnote">*Any extractions and more advanced dental procedures if required will incur an additional cost that will be discussed with your prior to the procedure.</p>
</main>
</body>
</html>
```